Block makes the buck for writing

We need a notepad in DIN A4 format which we can give to our customers at events. We, KORVANE, are active in the field of safe electrical engineering and offer software, hardware, academia and consulting in this field. With our software can be z. For example, you can quickly and easily inventory and document all equipment and equipment. Every tool must be checked in Germany and the test repeated at regular intervals. The appropriate test specifications are stored in our software. In addition to the software, we also offer measuring and testing equipment. In our academy, we also offer seminars on various areas of safe electrical engineering. Our consulting advises companies on the establishment of a legally compliant company organization. If necessary, our experts also take on the temporary function of external responsible electrician. So we offer an all-round package concerning safe electrical engineering. KORVANE makes working with electricity safe. Every year we offer an event with different workshops. There the users of our software are invited. You can exchange ideas with our lecturers and experts and exchange experiences and tips with each other. For this event we need a writing pad where participants can take their notes throughout the day. In addition, the block should also be used by customers. But it would be nice if he had a special feature / a special feature by which he is particularly happy to use. As basic the block should be branded with our logo and our URL (korvane.de).

```html
<!DOCTYPE html>
<html lang="de">
<head>
<meta charset="utf-8">
<title>KORVANE Notepad</title>
<link href="https://fonts.googleapis.com/css2?family=Roboto:wght@400;700&display=swap" rel="stylesheet">
<style>
  :root {
    --backdrop: #2b2c30;
    --paper: #ececed;
    --ink: #3c3c3b;
    --rule: #c3c3c5;
    --accent: #d4751f;
    --watermark: #dedee0;
  }
  * { margin: 0; padding: 0; box-sizing: border-box; }
  html, body {
    width: 1200px; height: 1200px; overflow: hidden;
    background: var(--backdrop);
    font-family: "Roboto", Arial, sans-serif;
  }
  .notepad {
    position: absolute; left: 197px; top: 30px;
    width: 806px; height: 1140px;
    background: var(--paper);
    overflow: hidden;
  }
  .brand {
    position: absolute; top: 52px; left: 0; width: 100%;
    display: flex; justify-content: center; align-items: center; gap: 14px;
  }
  .brand-name {
    font-weight: 700; font-size: 44px; letter-spacing: -0.5px;
    color: var(--ink); line-height: 1;
  }
  .brand-dot {
    width: 52px; height: 60px; border-radius: 50%;
    background: var(--accent);
  }
  .watermark {
    position: absolute; left: 196px; top: 325px;
    width: 414px; height: 490px; border-radius: 50%;
    background: var(--watermark); opacity: 0.6;
  }
  .rules { position: absolute; left: 0; top: 0; }
  .footer {
    position: absolute; left: 97px; top: 1064px;
    display: flex; align-items: center;
    font-size: 15.5px; line-height: 20px; color: var(--ink);
  }
  .footer-group { display: flex; flex-direction: column; padding: 0 18px; }
  .footer-group:first-child { padding-left: 0; }
  .footer-group + .footer-group { border-left: 1px solid #9a9a9a; }
  .contact-line { display: flex; align-items: center; gap: 8px; }
  .contact-line svg { width: 12px; height: 12px; flex: none; }
  .base-band {
    position: absolute; left: 0; bottom: 0; width: 100%; height: 11px;
    background: var(--accent);
  }
</style>
</head>
<body>
<main class="notepad">
  <header class="brand">
    <span class="brand-name">KORVANE</span>
    <span class="brand-dot"></span>
  </header>

  <div class="watermark" role="img" aria-label="Faint brand circle behind the writing lines"></div>

  <svg class="rules" width="806" height="1140" viewBox="0 0 806 1140" fill="none" stroke="#c3c3c5" stroke-width="1">
    <g id="line-set">
      <line x1="85" y1="165" x2="721" y2="165"/><circle cx="82" cy="165" r="2.5"/><circle cx="724" cy="165" r="2.5"/>
      <line x1="85" y1="210" x2="721" y2="210"/><circle cx="82" cy="210" r="2.5"/><circle cx="724" cy="210" r="2.5"/>
      <line x1="85" y1="254" x2="721" y2="254"/><circle cx="82" cy="254" r="2.5"/><circle cx="724" cy="254" r="2.5"/>
      <line x1="85" y1="299" x2="721" y2="299"/><circle cx="82" cy="299" r="2.5"/><circle cx="724" cy="299" r="2.5"/>
      <line x1="85" y1="344" x2="721" y2="344"/><circle cx="82" cy="344" r="2.5"/><circle cx="724" cy="344" r="2.5"/>
      <line x1="85" y1="388" x2="721" y2="388"/><circle cx="82" cy="388" r="2.5"/><circle cx="724" cy="388" r="2.5"/>
      <line x1="85" y1="433" x2="721" y2="433"/><circle cx="82" cy="433" r="2.5"/><circle cx="724" cy="433" r="2.5"/>
      <line x1="85" y1="477" x2="721" y2="477"/><circle cx="82" cy="477" r="2.5"/><circle cx="724" cy="477" r="2.5"/>
      <line x1="85" y1="522" x2="721" y2="522"/><circle cx="82" cy="522" r="2.5"/><circle cx="724" cy="522" r="2.5"/>
      <line x1="85" y1="567" x2="721" y2="567"/><circle cx="82" cy="567" r="2.5"/><circle cx="724" cy="567" r="2.5"/>
      <line x1="85" y1="611" x2="721" y2="611"/><circle cx="82" cy="611" r="2.5"/><circle cx="724" cy="611" r="2.5"/>
      <line x1="85" y1="656" x2="721" y2="656"/><circle cx="82" cy="656" r="2.5"/><circle cx="724" cy="656" r="2.5"/>
      <line x1="85" y1="700" x2="721" y2="700"/><circle cx="82" cy="700" r="2.5"/><circle cx="724" cy="700" r="2.5"/>
      <line x1="85" y1="745" x2="721" y2="745"/><circle cx="82" cy="745" r="2.5"/><circle cx="724" cy="745" r="2.5"/>
      <line x1="85" y1="790" x2="721" y2="790"/><circle cx="82" cy="790" r="2.5"/><circle cx="724" cy="790" r="2.5"/>
      <line x1="85" y1="834" x2="721" y2="834"/><circle cx="82" cy="834" r="2.5"/><circle cx="724" cy="834" r="2.5"/>
      <line x1="85" y1="879" x2="721" y2="879"/><circle cx="82" cy="879" r="2.5"/><circle cx="724" cy="879" r="2.5"/>
      <line x1="85" y1="923" x2="721" y2="923"/><circle cx="82" cy="923" r="2.5"/><circle cx="724" cy="923" r="2.5"/>
      <line x1="85" y1="968" x2="721" y2="968"/><circle cx="82" cy="968" r="2.5"/><circle cx="724" cy="968" r="2.5"/>
      <line x1="85" y1="1012" x2="721" y2="1012"/><circle cx="82" cy="1012" r="2.5"/><circle cx="724" cy="1012" r="2.5"/>
    </g>
  </svg>

  <footer class="footer">
    <div class="footer-group">
      <span class="contact-line">
        <svg viewBox="0 0 12 12" fill="none" stroke="#d4751f" stroke-width="1.3"><path d="M2.5 1.5l2 2-1 1.3c.6 1.3 1.5 2.2 2.7 2.7l1.3-1 2 2-1.3 1.5C5.5 10 2 6.5 1 2.8z"/></svg>
        +49 261 555 20 140
      </span>
      <span class="contact-line">
        <svg viewBox="0 0 12 12" fill="#d4751f"><rect x="3" y="1" width="6" height="3"/><rect x="1" y="4.5" width="10" height="4.5" rx="1"/><rect x="3" y="8" width="6" height="3" fill="#ececed" stroke="#d4751f"/></svg>
        +49 261 555 20 141
      </span>
    </div>
    <div class="footer-group">
      <span class="contact-line">
        <svg viewBox="0 0 12 12" fill="none" stroke="#d4751f" stroke-width="1.1"><rect x="1" y="2.5" width="10" height="7"/><path d="M1 2.5l5 4 5-4"/></svg>
        info@korvane.de
      </span>
      <span class="contact-line">
        <svg viewBox="0 0 12 12" fill="none" stroke="#d4751f" stroke-width="1"><circle cx="6" cy="6" r="5"/><ellipse cx="6" cy="6" rx="2.2" ry="5"/><path d="M1 6h10M2 3.5h8M2 8.5h8"/></svg>
        www.korvane.de
      </span>
    </div>
    <div class="footer-group">
      <span>KORVANE Holding GmbH</span>
      <span>Lindenweg 14, 56070 Neustadt</span>
    </div>
  </footer>

  <div class="base-band"></div>
</main>
</body>
</html>
```